Business Cards

Business card design for my company.
I would like the card's background colour to be black. You can also see our web site to get an idea of our brand. https://www.tmwhomecrafting.com.au/
- Name
- Email

```html
<!DOCTYPE html>
<html lang="en">
<head>
<meta charset="utf-8">
<title>TMW Home Crafting — Business Cards</title>
<link href="https://fonts.googleapis.com/css2?family=Roboto:wght@400;500;700&display=swap" rel="stylesheet">
<style>
  :root {
    --canvas-bg: #2c2c2c;
    --card-black: #000000;
    --brand-green: #0e9a48;
    --text-white: #f2f2f2;
    --band-white: #ffffff;
  }
  * { box-sizing: border-box; margin: 0; padding: 0; }
  html, body { width: 1200px; height: 875px; overflow: hidden; }
  body {
    background: var(--canvas-bg);
    font-family: "Roboto", sans-serif;
    position: relative;
  }
  .card {
    position: absolute;
    width: 530px;
    height: 310px;
    background: var(--card-black);
    border-radius: 18px;
    overflow: hidden;
    top: 282px;
    box-shadow: 0 18px 40px rgba(0,0,0,.45);
  }
  .card--front { left: 50px; }
  .card--back { left: 620px; }

  .brand-name {
    display: flex;
    align-items: center;
    gap: 10px;
    color: var(--text-white);
    font-weight: 700;
    letter-spacing: .04em;
    text-transform: uppercase;
    white-space: nowrap;
  }
  .brand-name__mark {
    width: 14px; height: 14px;
    background: var(--brand-green);
    flex: none;
  }
  .card--front .brand-name {
    position: absolute;
    left: 50%; top: 50%;
    transform: translate(-50%, -50%);
    font-size: 30px;
  }
  .card--front .brand-name__mark { width: 20px; height: 20px; }

  .card--back .brand-name {
    position: absolute;
    left: 24px; top: 168px;
    font-size: 16px;
    gap: 8px;
  }
  .card--back .brand-name__mark { width: 12px; height: 12px; }
  .divider {
    position: absolute;
    left: 256px; top: 46px;
    width: 1px; height: 190px;
    background: var(--brand-green);
  }
  .contact {
    position: absolute;
    left: 280px; top: 50px;
    color: var(--text-white);
  }
  .contact__name {
    color: var(--brand-green);
    font-size: 23px;
    font-weight: 700;
  }
  .contact__role {
    font-size: 13px;
    margin-top: 4px;
    margin-bottom: 16px;
  }
  .contact__list { list-style: none; font-size: 12.5px; }
  .contact__list li {
    display: flex; align-items: center; gap: 9px;
    margin-bottom: 8px;
  }
  .contact__list svg { width: 13px; height: 13px; fill: var(--brand-green); flex: none; }
  .contact__address {
    font-size: 12.5px; line-height: 1.45;
    margin-top: 12px; margin-left: 22px;
  }
  .card__band {
    position: absolute; left: 0; bottom: 0;
    width: 530px; height: 30px;
  }
</style>
</head>
<body>
  <section class="card card--front" aria-label="Card front">
    <div class="brand-name"><span class="brand-name__mark"></span>TMW Home Crafting</div>
  </section>

  <section class="card card--back" aria-label="Card back">
    <div class="brand-name"><span class="brand-name__mark"></span>TMW Home Crafting</div>
    <div class="divider"></div>
    <div class="contact">
      <p class="contact__name">Daniel Harper</p>
      <p class="contact__role">Owner</p>
      <ul class="contact__list">
        <li>
          <svg viewBox="0 0 24 24" aria-hidden="true"><path d="M6.6 10.8a15.1 15.1 0 0 0 6.6 6.6l2.2-2.2c.3-.3.7-.4 1-.2 1.1.4 2.3.6 3.6.6.6 0 1 .4 1 1V20c0 .6-.4 1-1 1C10.6 21 3 13.4 3 4c0-.6.4-1 1-1h3.5c.6 0 1 .4 1 1 0 1.3.2 2.5.6 3.6.1.3 0 .7-.2 1z"/></svg>
          (407) 555-0143
        </li>
        <li>
          <svg viewBox="0 0 24 24" aria-hidden="true"><path d="M2 5h20v14H2zm2 2v.5l8 5 8-5V7l-8 5z"/></svg>
          hello@tmwhomecrafting.com.au
        </li>
        <li>
          <svg viewBox="0 0 24 24" aria-hidden="true"><path d="M12 2a10 10 0 1 0 0 20 10 10 0 0 0 0-20zm0 2c1 0 2.3 2 2.8 5H9.2C9.7 6 11 4 12 4zm-3 7h6a17 17 0 0 1 0 2H9a17 17 0 0 1 0-2zm-5 0h3a19 19 0 0 0 0 2H4a8 8 0 0 1 0-2zm13 0h3a8 8 0 0 1 0 2h-3a19 19 0 0 0 0-2zM9.2 15h5.6c-.5 3-1.8 5-2.8 5s-2.3-2-2.8-5z"/></svg>
          www.tmwhomecrafting.com.au
        </li>
      </ul>
      <p class="contact__address">421, Address line goes here<br>45452, Country name</p>
    </div>
    <svg class="card__band" viewBox="0 0 530 30" preserveAspectRatio="none" aria-hidden="true">
      <polygon points="0,24 300,24 296,30 0,30" fill="var(--band-white)"/>
      <polygon points="304,14 530,14 530,30 296,30" fill="var(--brand-green)"/>
    </svg>
  </section>
</body>
</html>
```